looking for sleek business card to standout from the crowd!

We are a young biotechnology company looking to help you personalize your health through understanding your genetic make up. We need you help in making a clean but sleek business card design using our new logo. The goal? Any time we give our cards out, people say "nice card!" The feel we are going for is "modern-techy". We don't want to come across as an old, giant pharma company, but not trying to be a hipster either.

Target Market(s)

healthcare and biotechnology industry.

Industry/Entity Type

Biotechnology

Contact Information for Business Card

Info to include on the card will be NAME, TITLE, EMAIL, PHONE. The companies website (www.corvalinbio.com) should also be on the card some where. Would like the logo, when printed, to be raised.

Requirements
Must have
• The logo we have attached in the color it is in. Fonts for text should lean toward more professional/tech.
Nice to have
• Prefer white/light color background
Should not have
• cartoons, landscape backgrounds images.

```html
<!DOCTYPE html>
<html lang="en">
<head>
<meta charset="utf-8">
<title>Corvalin Business Card</title>
<link href="https://fonts.googleapis.com/css2?family=Jost:wght@400;500;800&display=swap" rel="stylesheet">
<style>
  :root {
    --backdrop: #dcdcdc;
    --card-front: #f0f0f0;
    --card-back: #278fda;
    --brand-text: #3b4046;
    --text-light: #ffffff;
  }
  * { margin: 0; padding: 0; box-sizing: border-box; }
  html, body {
    width: 1200px;
    height: 1007px;
    overflow: hidden;
    background: var(--backdrop);
    font-family: "Jost", sans-serif;
  }
  .canvas {
    position: relative;
    width: 1200px;
    height: 1007px;
  }
  .card {
    position: absolute;
    width: 620px;
    height: 360px;
    box-shadow: 0 4px 10px rgba(0,0,0,0.12);
  }
  .card-front {
    left: 290px;
    top: 80px;
    background: var(--card-front);
    display: flex;
    align-items: center;
    justify-content: center;
  }
  .brand-name {
    font-weight: 500;
    font-size: 52px;
    letter-spacing: 3px;
    color: var(--brand-text);
  }
  .card-back {
    left: 290px;
    top: 560px;
    background: var(--card-back);
    color: var(--text-light);
    text-align: center;
    padding-top: 108px;
  }
  .person-name {
    font-weight: 800;
    font-size: 30px;
    line-height: 1;
    text-shadow: 0 2px 2px rgba(0,0,0,0.2);
  }
  .person-title {
    font-weight: 400;
    font-size: 11px;
    margin-top: 8px;
  }
  .contact {
    list-style: none;
    margin-top: 26px;
    font-weight: 500;
    font-size: 13px;
    line-height: 22px;
  }
</style>
</head>
<body>
<main class="canvas">
  <section class="card card-front">
    <span class="brand-name">CORVALIN</span>
  </section>
  <section class="card card-back">
    <h1 class="person-name">Daniel Reyes Hart</h1>
    <p class="person-title">Founder &amp; CEO</p>
    <ul class="contact">
      <li>TEL: 37281506290</li>
      <li>danielhart@corvalinbio.com</li>
      <li>www.corvalinbio.com</li>
    </ul>
  </section>
</main>
</body>
</html>
```